New business leaflet

Flyers to attach to cars/vans in local area letting them know of the large format print co. In the area.
Printers and installers of vehicle livery , builders signage such as correx boards and hoarding boards , building wraps and banners,

See our website
Www.kvp-ltd.com

Be different!!

Target Market(s)

local business , promote self advertising

Industry/Entity Type

Building

Requirements
Must have
• Colorful and bold
Nice to have
• Be different

```html
<!DOCTYPE html>
<html lang="en">
<head>
<meta charset="utf-8">
<title>KVP Limited – Large Format Print Leaflet</title>
<link rel="stylesheet" href="https://fonts.googleapis.com/css2?family=Arimo:wght@400;700&family=Cinzel:wght@900&display=swap">
<style>
:root{
  --ink:#000;
  --paper:#fff;
  --red:#e8232a;
  --orange:#f7a11a;
  --amber:#f6c21a;
  --blue:#3c6fb6;
  --teal:#4fc4c0;
  --green:#5aa83a;
  --lime:#b8d432;
  --yellow:#f1ea1e;
  --pink:#e8288a;
  --cream:#fdf3e4;
  --sans:"Arimo", Arial, Helvetica, sans-serif;
  --display:"Cinzel", Georgia, serif;
}
*{box-sizing:border-box;margin:0;padding:0}
html,body{width:927px;height:1200px;overflow:hidden;background:var(--paper)}
.leaflet{position:relative;width:927px;height:1200px;font-family:var(--sans);background:var(--paper)}
.masthead{position:absolute;left:0;top:0;width:927px;height:418px;background:var(--ink);color:var(--paper)}
.brand-title{position:absolute;top:48px;width:100%;text-align:center;font-size:70px;font-weight:700;line-height:1}
.tagline{position:absolute;top:114px;width:100%;text-align:center;font-size:27.5px;font-weight:700;line-height:32px}
.intro{position:absolute;left:30px;top:206px;width:585px;font-size:19.5px;line-height:24.5px}
.intro p+p{margin-top:24px}
.logo-panel{position:absolute;left:646px;top:184px;width:247px;height:201px;background:var(--paper);display:flex;align-items:center;justify-content:center;gap:12px}
.logo-mark{width:26px;height:26px;border-radius:50%;background:var(--pink)}
.logo-name{font-size:36px;font-weight:700;color:var(--ink)}
.web{position:absolute;left:646px;width:247px;top:392px;text-align:center;font-size:18px}
.service{position:absolute;color:var(--paper);font-size:16.5px;line-height:23.5px;padding:38px 4px 0 5px}
.service-tab{position:absolute;top:0;height:26px;background:var(--paper);border:1.5px solid var(--ink);border-top:none;color:var(--ink);font-family:var(--display);font-weight:900;font-size:15px;letter-spacing:.6px;text-transform:uppercase;text-align:center;line-height:26px}
.service .photo{position:absolute;display:block}
.signage{left:15px;top:428px;width:282px;height:299px;background:linear-gradient(180deg,var(--red),var(--orange) 55%,var(--amber))}
.vehicle{left:309px;top:428px;width:301px;height:299px;padding-left:15px;padding-right:14px;background:linear-gradient(180deg,var(--blue),var(--teal))}
.correx{left:625px;top:428px;width:290px;height:299px;padding-left:0;background:linear-gradient(180deg,var(--green),var(--lime) 50%,var(--yellow))}
.banners{left:15px;top:738px;width:282px;height:298px;background:linear-gradient(180deg,var(--orange),var(--red))}
.hoarding{left:309px;top:738px;width:301px;height:298px;padding-left:10px;padding-right:12px;background:linear-gradient(180deg,var(--teal),var(--blue))}
.wraps{left:625px;top:738px;width:290px;height:298px;padding-left:11px;background:linear-gradient(180deg,var(--yellow),var(--lime) 50%,var(--green))}
.board-art{float:left;width:118px;height:184px;margin:0 15px 0 15px;background:linear-gradient(160deg,#e6e31e,#3a9fc9 55%,#2a2150)}
.contact{position:absolute;left:0;top:1046px;width:927px;height:154px;background:linear-gradient(90deg,var(--pink),#f3a6cd 65%,var(--cream));text-align:center;color:var(--ink)}
.contact h2{font-family:var(--display);font-weight:900;font-size:29px;margin-top:6px;line-height:36px;text-transform:uppercase}
.contact p{font-size:23.5px;font-weight:700;line-height:29px}
</style>
</head>
<body>
<main class="leaflet">
  <header class="masthead">
    <h1 class="brand-title">KVP Limited</h1>
    <p class="tagline">A printing company with over 50 years experience in Screen<br>Print and over 10 years experience in Digital Print</p>
    <div class="intro">
      <p>We are experts in printing difficult substrate such as corru-<br>gated boards, uncoated boards and papers, display boards, plastics, metals and glass, we also do the run of the mill self cling/self adhesive, rigid pvc’s.</p>
      <p>With the ability to handle runs into the 1000’s, KVP will deliver first class results, on time and on budget.</p>
    </div>
    <div class="logo-panel"><span class="logo-mark"></span><span class="logo-name">KVP Ltd</span></div>
    <p class="web">www.kvp-ltd.com</p>
  </header>

  <section class="service signage">
    <h3 class="service-tab" style="left:20px;width:228px">Builders Signage</h3>
    <p>KVP builders signage is designed around you and your site to ensure you make an impact and grab passing customers attention through ef-fective visual communication.</p>
    <div class="photo" role="img" aria-label="Building site entrance with printed signage" style="left:40px;top:165px;width:202px;height:121px;background:linear-gradient(180deg,#8a9bb0,#b3262c 55%,#7a7570)"></div>
  </section>

  <section class="service vehicle">
    <h3 class="service-tab" style="left:32px;width:240px">Vehicle Graphics</h3>
    <p>KVP are Specialists in commercial fleet livery so whether it be 1 or 100 vehicles, KVP print and install high quality graphics on time and to your budget.</p>
    <div class="photo" role="img" aria-label="Van wrapped in printed livery" style="left:49px;top:165px;width:201px;height:107px;background:linear-gradient(180deg,#d8d6d2,#3a3a3c 60%,#6b6f73)"></div>
  </section>

  <section class="service correx">
    <h3 class="service-tab" style="left:23px;width:244px">Correx Boards</h3>
    <div class="board-art" role="img" aria-label="Printed correx site board"></div>
    <p>Full colour high impact correx boards are printed using vibrant durable inks. We print site boards, safety signs as well as directional signs for your site.</p>
  </section>

  <section class="service banners">
    <h3 class="service-tab" style="left:20px;width:228px">Banners</h3>
    <p>We produce full colour, digitally printed banners at low prices. PVC and mesh banners can be fitted to scaffold, fencing and hoardings on any site.</p>
    <div class="photo" role="img" aria-label="Banner mounted on a site fence" style="left:40px;top:165px;width:202px;height:120px;background:linear-gradient(180deg,#c9ccd0,#e8701c 45%,#1a1a1a 70%,#5d6a4a)"></div>
  </section>

  <section class="service hoarding">
    <h3 class="service-tab" style="left:32px;width:240px">Hoarding Boards</h3>
    <p>Printed hoardings add desirability to your development while promoting your company and services. Boards are printed in a variety of sizes and fitted by our installers.</p>
    <div class="photo" role="img" aria-label="Printed hoarding boards around a building site" style="left:43px;top:167px;width:202px;height:105px;background:linear-gradient(180deg,#e4e6e8,#c8ccd0 70%,#7d8084)"></div>
  </section>

  <section class="service wraps">
    <h3 class="service-tab" style="left:23px;width:244px">Building Wraps</h3>
    <p>Whether you are looking for a full building wrap, scaffold wrap or printed mesh we are able to help. Using digital technology we print large images onto wrap panels.</p>
    <div class="photo" role="img" aria-label="Scaffold covered in a printed building wrap" style="left:45px;top:167px;width:204px;height:105px;background:linear-gradient(90deg,#e9e9ea,#c7352c 45%,#e6a23a 70%,#ececec)"></div>
  </section>

  <footer class="contact">
    <h2>Contact</h2>
    <p>Address: 14 Farley Road, Merton, Surrey, SM4 7QJ</p>
    <p>Tel: 020 8391 4427 Fax: 020 8391 4427</p>
    <p>E-Mail: info@kvp-ltd.com</p>
  </footer>
</main>
</body>
</html>
```